Drinking Water Protection Postcard Series

Design a series of 3 themed postcards that will be mailed in succession for a pilot project. Audience: to reach water operators who are responsible for managing very small public water systems (serving less than 1000 people in Pennsylvania). Purpose: Encourage small water systems to enter into a voluntary program known as "Brightmere Wellhead Care for Hamlet Utilities" that is available at no out of pocket cost from Harlow Bureau of Habitat Stewardship (HBHS). Source Water Protection helps protect public health by preventing contaminants from entering the rivers, streams and groundwater on which the public depends for source of drinking water. Source water protection safeguards public health, makes efficient use of limited financial resources (prevention is cheaper than water treatment or loss of a well), and has a positive impact on the environment as a whole. Slogan is: "Safe Drinking Water Starts at the Source." A Source Water Protection program maps out where your drinking water comes from, shows ways to stop pollution before it starts, and helps plan for water emergencies.
We have a logo for the program (and more info) that can be seen at www.brightmerewellhead.example.org and is attached. We are considering a tag line like: "Show you care. Get a Source Water Protection Plan for your water system." Would like to see designs that use the colors blue and green, and families, a glass of water to communicate good stewardship is smart business. Many small water systems are privately owned mobile home parks.
Reason: Some designers emailed they were going to submit, but I don't believe we received their designs yet. Thank you all for your work.
Sorry for the delay in responding. 9/30 was year end for us which took priority over our new projects. We are getting back on track and have sent designs out for review and input from our small nonprofit team. Thanks for your patience, and if you have had any other inspirations that may encourage water systems to protect their raw drinking water sources out in the watershed, please send them along; we will be reviewing this week. Preventing pollution up front is much cheaper and safer than trying to treat for every contaminant at the water treatment plant. Many thanks.
about 95% mail blue collar adults; aged 25 - 65 in more rural areas of Pennsylvania.
Water Treatment

```html
<!DOCTYPE html>
<html lang="en">
<head>
<meta charset="utf-8">
<title>Brightmere Wellhead Care Postcard</title>
<link rel="stylesheet" href="https://fonts.googleapis.com/css2?family=Arimo:wght@400;700&display=swap">
<style>
  :root {
    --navy: #13306b;
    --royal: #1f5aa8;
    --sky: #6fa7da;
    --teal: #1fa99a;
    --red: #e0161d;
    --white: #ffffff;
    --panel: rgba(255,255,255,0.8);
    --forest: #3d6a34;
    --forest-dark: #2a4e27;
    --rapids: #e9f2f6;
    --river: #8fb6c8;
    --warm: #d9b394;
    --shirt: #8fa870;
  }
  * { margin: 0; padding: 0; box-sizing: border-box; }
  html, body { width: 1200px; height: 773px; overflow: hidden; background: var(--white); }
  body { font-family: "Arimo", Arial, sans-serif; }
  .postcard { position: relative; width: 1200px; height: 773px; overflow: hidden; background: var(--white); }

  .scene-photo {
    position: absolute; left: 0; top: 80px; width: 1200px; height: 640px;
    background:
      radial-gradient(ellipse 330px 240px at 320px 560px, rgba(217,179,148,0.95), rgba(217,179,148,0) 75%),
      radial-gradient(ellipse 200px 170px at 110px 600px, rgba(143,168,112,0.9), rgba(143,168,112,0) 75%),
      radial-gradient(ellipse 260px 90px at 560px 360px, rgba(233,242,246,0.95), rgba(233,242,246,0) 80%),
      radial-gradient(ellipse 300px 110px at 1050px 420px, rgba(233,242,246,0.9), rgba(233,242,246,0) 80%),
      radial-gradient(ellipse 250px 120px at 640px 170px, rgba(42,78,39,0.9), rgba(42,78,39,0) 80%),
      linear-gradient(180deg, #9cc0d6 0%, #6d9a63 14%, var(--forest) 28%, var(--forest-dark) 36%, var(--river) 46%, var(--rapids) 58%, #b5cfdb 70%, #c8b7a3 86%, #a98d74 100%);
  }
  .swooshes { position: absolute; inset: 0; width: 1200px; height: 773px; }

  .logo-frame {
    position: absolute; left: 55px; top: 35px; width: 427px; height: 278px;
    background: var(--teal); padding: 12px;
  }
  .logo-inner {
    width: 100%; height: 100%; background: var(--white);
    display: flex; align-items: center; justify-content: center; gap: 14px;
  }
  .logo-mark { width: 26px; height: 26px; border-radius: 50%; background: var(--royal); flex: none; }
  .logo-name { font-weight: 700; font-size: 34px; line-height: 1.15; color: var(--navy); text-align: center; }

  .info-panel {
    position: absolute; left: 729px; top: 0; width: 395px; height: 650px;
    background: var(--panel); padding: 22px 14px 0 24px;
  }
  .headline { text-align: center; font-weight: 700; font-size: 32px; line-height: 1.17; color: var(--navy); margin-left: -10px; }
  .headline .program { color: var(--red); display: block; }
  .services { margin-top: 44px; }
  .services h2 {
    font-size: 23px; color: var(--red); font-weight: 700;
    display: inline-block; border-bottom: 3px solid var(--red); padding-bottom: 1px; margin-bottom: 20px;
  }
  .services ul { width: 310px; }
  .services li { list-style: none; color: var(--navy); font-weight: 700; font-size: 21px; line-height: 1.38; margin-bottom: 28px; }

  .web-address {
    position: absolute; left: 735px; top: 690px; width: 400px; text-align: center;
    font-weight: 700; font-size: 23px; color: var(--teal);
  }
</style>
</head>
<body>
<main class="postcard">
  <div class="scene-photo" role="img" aria-label="Photograph of a smiling family of five gathered in front of a rushing whitewater river with forested banks"></div>

  <svg class="swooshes" viewBox="0 0 1200 773" aria-hidden="true">
    <path d="M0 0 L1200 0 L1200 75 C760 60 330 110 0 150 Z" fill="var(--white)"/>
    <path d="M0 150 C330 110 760 60 1200 75 L1200 105 C760 95 330 150 0 190 Z" fill="var(--royal)"/>
    <path d="M0 190 C330 150 760 95 1200 105 L1200 125 C760 120 330 170 0 215 Z" fill="var(--sky)" opacity="0.85"/>
    <path d="M0 715 C350 700 780 680 1200 595 L1200 773 L0 773 Z" fill="var(--white)"/>
    <path d="M0 712 C360 700 780 680 1200 600 L1200 650 C780 700 380 722 0 735 Z" fill="var(--navy)"/>
    <path d="M480 660 C780 645 1000 610 1200 560 L1200 600 C1000 635 780 660 480 660 Z" fill="var(--teal)"/>
    <path d="M1200 700 L1200 773 L1140 773 C1170 750 1190 725 1200 700 Z" fill="var(--royal)"/>
  </svg>

  <div class="logo-frame">
    <div class="logo-inner">
      <span class="logo-mark"></span>
      <span class="logo-name">Brightmere<br>Wellhead Care</span>
    </div>
  </div>

  <section class="info-panel">
    <h1 class="headline">Did you know that you can get a
      <span class="program">Brightmere Wellhead Care for Hamlet Utilities</span>
      at NO COST to you !!</h1>
    <div class="services">
      <h2>Our Services:</h2>
      <ul>
        <li>Map out where your drinking water comes from</li>
        <li>Learn ways to stop pollution before it starts</li>
        <li>Get assistance with planning for water emergencies.</li>
      </ul>
    </div>
  </section>

  <p class="web-address">www.brightmerewellhead.example.org</p>
</main>
</body>
</html>
```